Quilvo Garage Doors Business Card

I need a Business Card for my garage door business:
Quilvo Garage Doors.
please add:
logo
phone number: 855-3-QUILVO
(853-392)

email: service@quilvogaragedoors.com
website: www.quilvogaragedoors.com

The attached image is recommendation ONLY.

```html
<!DOCTYPE html>
<html lang="en">
<head>
<meta charset="utf-8">
<title>Quilvo Garage Doors – Business Card</title>
<link rel="stylesheet" href="https://fonts.googleapis.com/css2?family=Open+Sans:wght@400;700&display=swap">
<style>
  :root {
    --backdrop: #2b2d31;
    --card-dark: #231f20;
    --brand-teal: #4fc6d2;
    --text-light: #e4e4e4;
    --text-white: #ffffff;
  }
  * { margin: 0; padding: 0; box-sizing: border-box; }
  html, body {
    width: 1200px;
    height: 864px;
    overflow: hidden;
  }
  body {
    background: var(--backdrop);
    font-family: "Open Sans", sans-serif;
    display: flex;
    flex-direction: column;
    align-items: center;
    justify-content: center;
    gap: 64px;
  }
  .card {
    width: 560px;
    height: 320px;
    border-radius: 2px;
    box-shadow: 0 10px 24px rgba(0, 0, 0, 0.35);
  }
  .card-front {
    background: var(--card-dark);
    display: flex;
    align-items: center;
    justify-content: center;
  }
  .brand {
    display: flex;
    align-items: center;
    gap: 22px;
  }
  .brand-square {
    width: 72px;
    height: 72px;
    background: var(--brand-teal);
    border-radius: 4px;
  }
  .brand-name {
    color: var(--text-light);
    font-size: 34px;
    font-weight: 400;
    letter-spacing: 0.2px;
  }
  .card-back {
    background: var(--brand-teal);
    color: var(--text-white);
    display: flex;
    flex-direction: column;
    align-items: center;
    justify-content: center;
    text-align: center;
  }
  .person-name {
    font-size: 20px;
    font-weight: 700;
    line-height: 1.1;
  }
  .person-title {
    font-size: 14px;
    font-weight: 400;
    margin-bottom: 40px;
  }
  .contact-line {
    font-size: 15px;
    font-weight: 400;
    line-height: 1.35;
  }
</style>
</head>
<body>
  <section class="card card-front" aria-label="Card front">
    <div class="brand">
      <span class="brand-square" aria-hidden="true"></span>
      <span class="brand-name">Quilvo Garage Doors</span>
    </div>
  </section>

  <section class="card card-back" aria-label="Card back">
    <p class="person-name">Marcus Ellery</p>
    <p class="person-title">Managing Director</p>
    <p class="contact-line">855-3-QUILVO</p>
    <p class="contact-line">service@quilvogaragedoors.com</p>
    <p class="contact-line">www.quilvogaragedoors.com</p>
  </section>
</body>
</html>
```